Marlowe Financial Inc
stationary & new business card
Professional
Derek Hollins
MBA, AAMS, CRPC, AIF
732 N Fern Ave
Pinecrest ID 99387
derek@marlowefinancialinc.com
www.marlowefinancialinc.com
**** see uploaded files for **** discloesures & footnotes needed on card, fax, email and letterhead
items that MUST be included

```html
<!DOCTYPE html>
<html lang="en">
<head>
<meta charset="utf-8">
<title>Marlowe Financial Inc — Business Card</title>
<link rel="stylesheet" href="https://fonts.googleapis.com/css2?family=Arimo:wght@400;700&display=swap">
<style>
  :root {
    --page-bg: #2a2a2a;
    --card-bg: #ffffff;
    --ink: #1f1f1f;
    --muted: #555555;
    --brand-blue: #1f5fa8;
    --accent-blue: #2b74c7;
    --faint-blue: #dce8f5;
  }
  * { margin: 0; padding: 0; box-sizing: border-box; }
  html, body { width: 1200px; height: 766px; overflow: hidden; }
  body {
    background: var(--page-bg);
    font-family: "Arimo", Arial, sans-serif;
    position: relative;
  }
  .card {
    position: absolute;
    width: 540px;
    height: 309px;
    background: var(--card-bg);
    overflow: hidden;
  }
  .card--front { left: 620px; top: 229px; }
  .card--back { left: 40px; top: 229px; }

  .brand {
    display: flex;
    align-items: center;
    gap: 10px;
  }
  .brand__mark {
    width: 28px;
    height: 28px;
    background: var(--brand-blue);
  }
  .brand__name {
    font-weight: 700;
    font-size: 17px;
    line-height: 1.05;
    color: var(--brand-blue);
    letter-spacing: 0.5px;
    text-transform: uppercase;
  }
  .card--front .brand { position: absolute; left: 26px; top: 36px; }

  .holder { position: absolute; right: 26px; top: 30px; text-align: right; }
  .holder__name { font-size: 22px; color: var(--ink); font-weight: 400; }
  .holder__creds { font-size: 8px; color: var(--muted); margin-top: 3px; letter-spacing: 0.3px; }

  .contact {
    position: absolute;
    right: 26px;
    bottom: 30px;
    text-align: right;
    font-size: 9px;
    line-height: 1.55;
    color: var(--ink);
  }
  .contact__address { margin-bottom: 8px; color: var(--muted); }
  .contact__label { color: var(--accent-blue); }

  .decor {
    position: absolute;
    border-radius: 50%;
    background: radial-gradient(circle, var(--faint-blue) 0%, rgba(220,232,245,0) 70%);
  }
  .card--front .decor { left: 150px; top: 175px; width: 160px; height: 160px; }
  .card--back .decor { right: -30px; bottom: -40px; width: 220px; height: 220px; }

  .card--back .brand {
    position: absolute;
    left: 50%;
    top: 120px;
    transform: translateX(-50%);
  }
  .web {
    position: absolute;
    left: 0; right: 0;
    top: 172px;
    text-align: center;
    font-size: 10px;
    color: var(--accent-blue);
  }
</style>
</head>
<body>
  <section class="card card--back" aria-label="Business card back">
    <div class="decor" role="img" aria-label="Faint brand decoration"></div>
    <div class="brand">
      <span class="brand__mark"></span>
      <span class="brand__name">Marlowe<br>Financial Inc</span>
    </div>
    <p class="web">www.marlowefinancialinc.com</p>
  </section>

  <section class="card card--front" aria-label="Business card front">
    <div class="decor" role="img" aria-label="Faint brand decoration"></div>
    <div class="brand">
      <span class="brand__mark"></span>
      <span class="brand__name">Marlowe<br>Financial Inc</span>
    </div>
    <div class="holder">
      <p class="holder__name">Derek Hollins</p>
      <p class="holder__creds">MBA, AAMS, CRPC, AIF</p>
    </div>
    <div class="contact">
      <p class="contact__address">732 N Fern Ave<br>Pinecrest ID 99387</p>
      <p><span class="contact__label">Toll free:</span> 1-877-555-0148</p>
      <p><span class="contact__label">Phone:</span> 509-555-0172</p>
      <p><span class="contact__label">Fax:</span> 509-555-0179</p>
      <p><span class="contact__label">Email:</span> derek@marlowefinancialinc.com</p>
    </div>
  </section>
</body>
</html>
```